Business Card for Quillmark Ledger - A cannabis publication for executives.

I'd like some business cards for Quillmark Ledger. The logo is done (great job!) and I need a card design I will use with PRINTLY. I made it a short project to allow time for printing before an event. These will be standard sized cards (final artwork size 3.66" x 2.16" at 300dpi) with a final card size of 3.5" x 2.0". (See PRINTLY.com if you need more info.) I might try rounded corners but am not sure yet. I think the design will work okay with rounded.

Quillmark Ledger will be a bi-weekly publication for the cannabis industry. It is targeted to investors and industry executives, not consumers or pot smokers. So our market is more B2B. However I am open to creativity and making the card something people remark on.

My contact for card:

Dana Merrow
Founder/CEO
dana@quillmarkledger.example

2740 Harlow Avenue
Boston MA 02135
(617)555-0194

Target Market(s)

Executives, Industry people and investors in the Cannabis sector.

Contact Information for Business Card

PRINTLY does do double sided and the second side can be the same or different images. Only one side is required but use of the second side would be a bonus.

Font styles to use
Serif
Sans Serif
Decorative

Colors

Designer to choose colors to be used in the design.

Requirements
Must have
• Logo, contact info
Nice to have
• Style and design to make the card stand out in a crowd.

```html
<!DOCTYPE html>
<html lang="en">
<head>
<meta charset="utf-8">
<title>Quillmark Ledger — Business Card</title>
<link rel="stylesheet" href="https://fonts.googleapis.com/css2?family=Libre+Baskerville:wght@700&family=Open+Sans:wght@400;600&display=swap">
<style>
  :root {
    --leaf-green: #7cb342;
    --ink-grey: #4a4a4a;
    --soft-grey: #6b6b6b;
    --card-white: #ffffff;
    --backdrop: #e9e7e3;
    --rule: #d9dccf;
  }
  * { box-sizing: border-box; margin: 0; padding: 0; }
  html, body {
    width: 1200px;
    height: 1200px;
    overflow: hidden;
    background: var(--backdrop);
  }
  .sheet {
    width: 1200px;
    height: 1200px;
    display: flex;
    flex-direction: column;
    align-items: center;
    justify-content: center;
    gap: 80px;
  }
  .card {
    width: 700px;
    height: 400px;
    background: var(--card-white);
    box-shadow: 0 6px 22px rgba(0,0,0,0.12);
    position: relative;
  }
  /* Front: brand side */
  .card--brand {
    display: flex;
    align-items: center;
    justify-content: center;
  }
  .brand {
    display: flex;
    align-items: center;
    gap: 18px;
  }
  .brand__square {
    width: 40px;
    height: 40px;
    background: var(--leaf-green);
  }
  .brand__name {
    font-family: "Libre Baskerville", Georgia, serif;
    font-weight: 700;
    font-size: 40px;
    color: var(--leaf-green);
  }
  /* Back: contact side */
  .card--contact .frame {
    position: absolute;
    inset: 22px;
    border: 2px solid var(--leaf-green);
    display: flex;
    flex-direction: column;
    align-items: center;
    padding-top: 44px;
    text-align: center;
  }
  .contact__name {
    font-family: "Libre Baskerville", Georgia, serif;
    font-weight: 700;
    font-size: 32px;
    letter-spacing: 1px;
    text-transform: uppercase;
    color: var(--leaf-green);
  }
  .contact__title {
    font-family: "Open Sans", Arial, sans-serif;
    font-size: 17px;
    color: var(--soft-grey);
    margin-top: 6px;
  }
  .contact__details {
    margin-top: 62px;
    font-family: "Open Sans", Arial, sans-serif;
    font-size: 19px;
    line-height: 1.5;
    color: var(--ink-grey);
  }
  .contact__rule {
    width: 440px;
    height: 1px;
    background: var(--rule);
    margin: 8px auto 6px;
  }
</style>
</head>
<body>
  <main class="sheet">
    <section class="card card--brand" aria-label="Card front">
      <div class="brand">
        <span class="brand__square"></span>
        <span class="brand__name">Quillmark Ledger</span>
      </div>
    </section>

    <section class="card card--contact" aria-label="Card back">
      <div class="frame">
        <h1 class="contact__name">Dana Merrow</h1>
        <p class="contact__title">Founder/CEO</p>
        <div class="contact__details">
          <p>(617)555-0194</p>
          <p>dana@quillmarkledger.example</p>
          <div class="contact__rule"></div>
          <p>2740 Harlow Avenue, Boston MA 02135</p>
        </div>
      </div>
    </section>
  </main>
</body>
</html>
```